Solar Billboard Design

We require a billboard 24ftx10ft in size for our solar company.
Artwork Requirement’s:
• Sent on PDF file
• At least 300 dpi
• Scaled to 25% of banner size (24ft x 10ft)
• Please allow at least 40mm space from the artwork edge to allow for any hems and eyelets. This will ensure any important text/images are not cropped/overlapped.
The billboard must have on it:
Solar & Battery Packages
From £8750
In Stock Now!
brightfieldpower.co.uk (must stand out)
________________________
I have attached our logo and some images. I'm not sure if they are good enough quality so you may need to use a stock image.
Kind regards,
Marcus
Target Market(s)
Men & Women aged 35-70, homeowners
Industry/Entity Type
Solar / Construction
Look and feel
Each slider illustrates characteristics of the customer's brand and the style your logo design should communicate.

```html
<!DOCTYPE html>
<html lang="en">
<head>
<meta charset="utf-8">
<title>Brightfield Power – Solar &amp; Battery Packages</title>
<link href="https://fonts.googleapis.com/css2?family=Montserrat:wght@300;500;700;800&display=swap" rel="stylesheet">
<style>
  :root {
    --green: #48b964;
    --charcoal: #464547;
    --ink: #231f20;
    --white: #ffffff;
    --page: #ffffff;
    --photo-light: #a0705c;
    --photo-dark: #3a3440;
  }
  * { margin: 0; padding: 0; box-sizing: border-box; }
  html, body { width: 1200px; height: 630px; overflow: hidden; background: var(--page); }
  body { font-family: "Montserrat", sans-serif; position: relative; }

  .billboard {
    position: absolute;
    left: 30px; top: 76px;
    width: 1140px; height: 478px;
    overflow: hidden;
    background: var(--white);
  }
  .billboard-shapes { position: absolute; inset: 0; width: 100%; height: 100%; }

  .brand {
    position: absolute; left: 62px; top: 46px;
    display: flex; align-items: center; gap: 22px;
  }
  .brand-mark { width: 54px; height: 54px; background: var(--green); }
  .brand-name {
    color: var(--charcoal); font-weight: 500;
    font-size: 27px; line-height: 1.14; letter-spacing: 0.14em;
    text-transform: uppercase;
  }

  .web-address {
    position: absolute; right: 25px; top: 36px;
    color: var(--ink); font-weight: 700; font-size: 37px; line-height: 1;
    letter-spacing: -0.01em;
  }
  .headline {
    position: absolute; right: 22px; top: 98px;
    color: var(--white); font-weight: 800; font-size: 64px; line-height: 1.18;
    text-align: right; text-transform: uppercase; letter-spacing: -0.01em;
  }
  .price {
    position: absolute; right: 18px; top: 268px;
    color: var(--white); display: flex; align-items: baseline; gap: 24px;
  }
  .price-from { font-weight: 300; font-size: 35px; }
  .price-amount { font-weight: 800; font-size: 86px; line-height: 1; letter-spacing: -0.02em; }

  .stock {
    position: absolute; right: 24px; top: 410px;
    color: var(--white); font-weight: 700; font-size: 40px; line-height: 1;
  }
</style>
</head>
<body>
  <main class="billboard">
    <svg class="billboard-shapes" viewBox="0 0 2220 930" preserveAspectRatio="none">
      <defs>
        <linearGradient id="photoTone" x1="0" y1="0" x2="0.6" y2="1">
          <stop offset="0" stop-color="var(--photo-light)"/>
          <stop offset="1" stop-color="var(--photo-dark)"/>
        </linearGradient>
      </defs>
      <path d="M0 0 H342 C220 30 90 90 0 165 Z" fill="var(--charcoal)"/>
      <path d="M1652 0 H2220 V930 H1400 L660 330 C900 120 1300 10 1652 0 Z" fill="var(--green)"/>
      <path role="img" aria-label="Photo of a tiled house roof fitted with black solar panels"
            d="M0 530 L582 270 L682 305 L1562 815 C1510 850 1460 890 1422 930 H0 Z"
            fill="url(#photoTone)"/>
      <path d="M1422 930 C1580 800 1760 720 1922 722 C2060 724 2160 745 2220 765 V930 Z" fill="var(--charcoal)"/>
    </svg>

    <div class="brand">
      <span class="brand-mark"></span>
      <span class="brand-name">Brightfield<br>Power<br>Group</span>
    </div>

    <p class="web-address">brightfieldpower.co.uk</p>
    <h1 class="headline">Solar &amp; Battery<br>Packages</h1>
    <p class="price"><span class="price-from">from</span><span class="price-amount">£8750</span></p>
    <p class="stock">In Stock Now!</p>
  </main>
</body>
</html>
```